Hula-Hoop dance entertainment sales and instruction by spin-wisp needs a business card

I need a 2 sided business card that is square (although this is not an absolute )for my self employed business as an independent artist. my business name is "Spin-Wisp" I teach how to hula-hoop classes, make and sell hula-hoops, provided entertainment at kids birthday parties, community events, corporate events and perform at artistic dance shows.
I would like to see spirals or curved lines in the card, and I would like the card to be seen as fun, spunky, flair and eye catching.

the card could double as a tag to go on the hoops i sell,

Target Market(s)

women age 20 - 50

Industry/Entity Type

Entertainment

Requirements
Must have
• Dena Marwick
www.spinwispdemo.com
555.014.7263
Nice to have
• I would like my image to be on one side of the card. so people can recognize me!

```html
<!DOCTYPE html>
<html lang="en">
<head>
<meta charset="utf-8">
<title>Spin-Wisp Business Card</title>
<link rel="stylesheet" href="https://fonts.googleapis.com/css2?family=Arimo:wght@400;700&family=Italianno&display=swap">
<style>
  :root {
    --page-bg: #e6e4e1;
    --card-bg: #ffffff;
    --card-edge: #f1f1f1;
    --ink: #1e1e1e;
    --purple: #5b1e78;
    --purple-deep: #3f1256;
    --purple-light: #7a3a98;
    --grey: #8f9296;
    --white: #ffffff;
  }
  * { box-sizing: border-box; margin: 0; padding: 0; }
  html, body { width: 1200px; height: 1001px; overflow: hidden; }
  body {
    background: var(--page-bg);
    font-family: "Arimo", Arial, sans-serif;
    color: var(--ink);
    position: relative;
  }
  .card {
    position: absolute;
    top: 90px;
    width: 470px;
    height: 820px;
    border-radius: 24px;
    background: linear-gradient(180deg, var(--card-bg) 0%, var(--card-edge) 100%);
    box-shadow: 0 6px 18px rgba(0,0,0,0.18);
    overflow: hidden;
  }
  .card--front { left: 100px; }
  .card--back { left: 630px; }

  .brand-mark {
    position: absolute;
    left: 0; right: 0;
    display: flex;
    align-items: center;
    justify-content: center;
    gap: 12px;
  }
  .brand-mark__dot {
    width: 22px; height: 22px;
    border-radius: 50%;
    background: var(--purple);
  }
  .brand-mark__name {
    font-family: "Italianno", cursive;
    font-size: 48px;
    line-height: 1;
    color: var(--ink);
  }
  .card--front .brand-mark { top: 80px; }
  .card--back .brand-mark { top: 70px; }

  .figures-illustration {
    position: absolute;
    left: 40px; top: 170px;
    width: 390px; height: 330px;
    border-radius: 8px;
    background: linear-gradient(180deg, #f6f6f6 0%, #e4e4e4 100%);
  }
  .front-swoosh {
    position: absolute;
    left: 0; top: 470px;
    width: 470px; height: 110px;
  }
  .wordmark {
    position: absolute;
    left: 0; right: 0;
    text-align: center;
    font-family: "Italianno", cursive;
    font-weight: 400;
    line-height: 1;
    color: var(--ink);
  }
  .card--front .wordmark { top: 612px; font-size: 96px; }
  .card--back .wordmark { top: 176px; font-size: 80px; }

  .back-curve {
    position: absolute;
    left: 0; top: 0;
    width: 470px; height: 820px;
  }
  .person-name {
    position: absolute;
    top: 318px; left: 0; right: 0;
    padding-left: 120px;
    text-align: center;
    font-size: 30px;
    color: var(--purple);
  }
  .portrait-photo {
    position: absolute;
    left: 268px; top: 420px;
    width: 190px; height: 140px;
    background: linear-gradient(135deg, #d9d9dc 0%, #b9b4b0 55%, #8e8f93 100%);
  }
  .contact-list {
    position: absolute;
    left: 34px; top: 664px;
    list-style: none;
    color: var(--white);
    font-size: 19px;
    line-height: 30px;
  }
  .contact-list li { display: flex; align-items: center; gap: 10px; }
  .contact-list svg { width: 14px; height: 14px; flex: none; }
</style>
</head>
<body>

<section class="card card--front">
  <div class="brand-mark">
    <span class="brand-mark__dot"></span>
    <span class="brand-mark__name">Spin-Wisp</span>
  </div>
  <div class="figures-illustration" role="img" aria-label="Sketch illustration of two flapper-style women, one spinning a hula hoop"></div>
  <svg class="front-swoosh" viewBox="0 0 470 110" aria-hidden="true">
    <defs>
      <linearGradient id="front-swoosh-fill" x1="0" x2="1">
        <stop offset="0" stop-color="#7a3a98"/>
        <stop offset="1" stop-color="#3f1256"/>
      </linearGradient>
    </defs>
    <path d="M0 40 C 120 60, 260 10, 470 38 L470 60 C 300 40, 150 90, 0 62 Z" fill="url(#front-swoosh-fill)"/>
  </svg>
  <div class="wordmark">Spin-Wisp</div>
</section>

<section class="card card--back">
  <svg class="back-curve" viewBox="0 0 470 820" aria-hidden="true">
    <defs>
      <linearGradient id="back-curve-fill" x1="0" y1="0" x2="1" y2="1">
        <stop offset="0" stop-color="#7a3a98"/>
        <stop offset="1" stop-color="#3f1256"/>
      </linearGradient>
    </defs>
    <path d="M0 390 C 60 560, 240 640, 470 640 L470 820 L0 820 Z" fill="url(#back-curve-fill)"/>
    <path d="M170 580 C 280 630, 390 640, 470 620 L470 652 C 370 660, 270 640, 170 580 Z" fill="var(--grey)"/>
  </svg>
  <div class="brand-mark">
    <span class="brand-mark__dot"></span>
    <span class="brand-mark__name">Spin-Wisp</span>
  </div>
  <div class="wordmark">Spin-Wisp</div>
  <div class="person-name">Dena Marwick</div>
  <div class="portrait-photo" role="img" aria-label="Photo of the performer holding a hula hoop"></div>
  <ul class="contact-list">
    <li>
      <svg viewBox="0 0 16 16"><path d="M3 1 L6 1 L7 5 L5 6.5 C6 9 7.5 10.5 9.5 11 L11 9 L15 10 L15 13 C15 14 14 15 13 15 C6 15 1 10 1 3 C1 2 2 1 3 1 Z" fill="#ffffff"/></svg>
      <span>555.014.7263</span>
    </li>
    <li>
      <svg viewBox="0 0 16 16"><rect x="1" y="3" width="14" height="10" fill="#ffffff"/><path d="M1 3 L8 9 L15 3" stroke="#5b1e78" stroke-width="1.4" fill="none"/></svg>
      <span>dena@spinwispdemo.com</span>
    </li>
    <li>
      <svg viewBox="0 0 16 16"><circle cx="8" cy="8" r="6.3" fill="none" stroke="#ffffff" stroke-width="1.4"/><path d="M1.7 8 H14.3 M8 1.7 C5 5 5 11 8 14.3 M8 1.7 C11 5 11 11 8 14.3" stroke="#ffffff" stroke-width="1.2" fill="none"/></svg>
      <span>www.spinwispdemo.com</span>
    </li>
    <li>
      <svg viewBox="0 0 16 16"><path d="M8 1 C5 1 3 3.2 3 6 C3 9.5 8 15 8 15 C8 15 13 9.5 13 6 C13 3.2 11 1 8 1 Z" fill="#ffffff"/><circle cx="8" cy="6" r="2" fill="#5b1e78"/></svg>
      <span>240 Sample Lane, Hoopton, Exampleville</span>
    </li>
  </ul>
</section>

</body>
</html>
```